Stationery Design Project

KT7 Staffing requires letterhead and business card designs for a company based in London. Just like the name, we're a management resourcing company, providing resources to third party companies. You can see www.kt7staffing-example.com for ideas on existing colour schemes and design concepts that have been implimented and agreed to. Ultimately the design should broadcast professionalism, safety and the concept of growth.

Target Market(s)

Financial institutes; friendly societies (All UK based)

Industry/Entity Type

Safety

Requirements
Must have
• Files produced should be print ready; and the text in them editable (eg address, name etc)

```html
<!DOCTYPE html>
<html lang="en">
<head>
<meta charset="utf-8">
<title>KT7 Staffing — Stationery Design Project</title>
<link rel="stylesheet" href="https://fonts.googleapis.com/css2?family=Arimo:wght@400;700&display=swap">
<style>
  :root {
    --brand-blue: #1f6f9f;
    --brand-deep: #165a84;
    --brand-light: #8ccbe8;
    --brand-pale: #d7eef8;
    --sky-top: #0d3a5c;
    --sky-mid: #3f86b8;
    --sky-low: #a9d4ee;
    --ink: #3a3a3a;
    --ink-soft: #6b6b6b;
    --paper: #ffffff;
    --page: #ffffff;
    --rule: #9a9a9a;
  }
  * { margin: 0; padding: 0; box-sizing: border-box; }
  html, body { width: 1200px; height: 900px; overflow: hidden; background: var(--page); }
  body { position: relative; font-family: "Arimo", Arial, sans-serif; color: var(--ink); }

  /* Letterhead */
  .letterhead { position: absolute; left: 45px; top: 68px; width: 582px; height: 747px; background: var(--paper); box-shadow: 0 0 0 1px #e3e3e3; overflow: hidden; }
  .letterhead__header { position: absolute; left: 0; top: 0; width: 582px; height: 150px; }
  .wordmark { position: absolute; font-weight: 700; letter-spacing: 0.02em; line-height: 1; }
  .letterhead .wordmark { left: 52px; top: 26px; font-size: 24px; color: var(--paper); }
  .letterhead__url { position: absolute; left: 52px; top: 66px; font-size: 8px; letter-spacing: 0.14em; color: var(--brand-pale); }
  .letterhead__body { position: absolute; left: 109px; top: 164px; width: 422px; }
  .section-title { font-size: 13px; font-weight: 700; color: var(--ink); margin-bottom: 18px; }
  .section-text { font-size: 8px; line-height: 11.5px; color: var(--ink); margin-bottom: 11px; }
  .section + .section { margin-top: 30px; }
  .sign-off { position: absolute; left: 109px; top: 615px; font-size: 8px; }
  .signature { position: absolute; left: 109px; top: 628px; width: 110px; height: 44px; background: linear-gradient(90deg, #f2f2f2, #e6e6e6); border-radius: 4px; }
  .letterhead__footer { position: absolute; left: 0; bottom: 0; width: 100%; height: 31px; background: var(--brand-blue); color: var(--paper); font-size: 7.5px; display: flex; align-items: center; padding-left: 108px; gap: 26px; }
  .footer-item { display: flex; align-items: center; gap: 5px; }
  .footer-item svg { width: 8px; height: 8px; fill: var(--paper); }

  /* Business cards */
  .card { position: absolute; top: 68px; width: 248px; height: 151px; overflow: hidden; border-radius: 4px; }
  .card--front { left: 645px; background: var(--paper); box-shadow: 0 0 0 1px #dfe9ef; }
  .card--back { left: 906px; background: var(--brand-pale); }
  .card__strip { position: absolute; left: 0; width: 100%; background: var(--brand-blue); }
  .card__strip--top { top: 0; height: 10px; }
  .card__strip--bottom { bottom: 0; height: 11px; color: var(--brand-pale); font-size: 5.5px; letter-spacing: 0.14em; display: flex; align-items: center; justify-content: center; }
  .card--front .wordmark { left: 14px; top: 36px; font-size: 13px; color: var(--brand-blue); }
  .card__person { position: absolute; left: 140px; top: 36px; }
  .card__name { font-size: 8px; font-weight: 700; color: var(--ink); }
  .card__role { font-size: 5.5px; color: var(--ink-soft); margin-top: 2px; }
  .card__contacts { position: absolute; left: 140px; top: 68px; font-size: 5px; line-height: 8.5px; color: var(--ink-soft); }
  .card__contacts svg { width: 5px; height: 5px; fill: var(--brand-blue); vertical-align: -0.5px; margin-right: 3px; }
  .card__skyline { position: absolute; left: 0; top: 0; width: 100%; height: 82px; background: linear-gradient(180deg, var(--sky-top) 0%, var(--sky-mid) 65%, var(--sky-low) 100%); }
  .card--back .wordmark { left: 62px; top: 90px; font-size: 14px; color: var(--brand-blue); }
  .card--back .card__strip--bottom { justify-content: flex-end; padding-right: 26px; }

  /* Project caption */
  .project-mark { position: absolute; left: 832px; top: 748px; font-size: 24px; font-weight: 700; color: var(--brand-blue); letter-spacing: 0.02em; }
  .project-rule { position: absolute; left: 832px; top: 807px; width: 368px; height: 1px; background: var(--rule); }
  .project-title { position: absolute; left: 834px; top: 814px; font-size: 21px; color: var(--ink-soft); }
</style>
</head>
<body>

<article class="letterhead">
  <svg class="letterhead__header" viewBox="0 0 582 150" aria-hidden="true">
    <defs>
      <linearGradient id="skyline-fill" x1="0" y1="0" x2="0" y2="1">
        <stop offset="0" stop-color="#0d3a5c"/>
        <stop offset="0.7" stop-color="#3f86b8"/>
        <stop offset="1" stop-color="#1f6f9f"/>
      </linearGradient>
      <linearGradient id="skyline-fade" x1="0" y1="0" x2="1" y2="0">
        <stop offset="0" stop-color="#1f6f9f"/>
        <stop offset="0.45" stop-color="#1f6f9f" stop-opacity="0"/>
      </linearGradient>
    </defs>
    <rect width="582" height="150" fill="#1f6f9f"/>
    <path d="M0 150 L0 122 Q210 72 582 112 L582 150 Z" fill="#8ccbe8"/>
    <path d="M0 150 L0 138 Q240 92 582 126 L582 150 Z" fill="#ffffff"/>
  </svg>
  <div role="img" aria-label="Photograph of a city financial district skyline at dusk" style="position:absolute;left:250px;top:0;width:332px;height:100px;background:linear-gradient(180deg,var(--sky-top),var(--sky-mid) 70%,var(--brand-blue));-webkit-mask-image:linear-gradient(90deg,transparent,#000 35%);mask-image:linear-gradient(90deg,transparent,#000 35%);"></div>
  <div class="wordmark">KT7 STAFFING</div>
  <div class="letterhead__url">www.kt7staffing-example.com</div>

  <div class="letterhead__body">
    <section class="section">
      <h2 class="section-title">ABOUT US</h2>
      <p class="section-text">Through a dedicated team of professionals, with at least fifteen years of experience in their various fields, we offer our clients a focused service of problem solving, key consultation and driving change for all of the challenges of modern business. Our unique approach means that our team of professionals work from the inside. They see the problems from the ground floor and are able to offer tailored advice on a range of business issues.</p>
    </section>
    <section class="section">
      <h2 class="section-title">OUR CULTURE</h2>
      <p class="section-text">KT7 Staffing is a multi-national company with clients in North America, Europe and Africa. We hire only seasoned professionals with at least 10 - 15 years of experience in their relevant fields. All of whom exemplify our core business values – Professionalism, Talent, Integrity and Loyalty.</p>
      <p class="section-text">Our professionals are guided by the innovative culture at KT7 Staffing, a culture which puts great emphasis on teamwork, results and flexibility. When our team of professionals go inside any business they do so with an open mind, ready to address any multitude of issues that may present themselves. Our custom approach is unique to each of our clients, ensuring the each client receives the best service possible.</p>
      <p class="section-text">Our work is results oriented. Because when our clients succeed, so do we.</p>
    </section>
    <section class="section">
      <h2 class="section-title">OUR LEADERSHIP</h2>
      <p class="section-text">Our leadership team possess a rich and diverse industry knowledge, delivering an unprecedented level of commitment and value to our customers.</p>
      <p class="section-text">We are currently updating our leadership team's profiles, please check back again soon.</p>
    </section>
  </div>

  <div class="sign-off">Director</div>
  <div class="signature" role="img" aria-label="Handwritten director signature"></div>

  <footer class="letterhead__footer">
    <span class="footer-item">14 Harrow Row, City of London</span>
    <span class="footer-item"><svg viewBox="0 0 10 10"><path d="M2 0.5 L4 0.5 L4.8 2.8 L3.6 3.8 Q4.6 5.6 6.2 6.4 L7.2 5.2 L9.5 6 L9.5 8 Q9.5 9.5 8 9.5 Q0.5 9 0.5 2 Q0.5 0.5 2 0.5 Z"/></svg>020 7946 0101</span>
    <span class="footer-item"><svg viewBox="0 0 10 10"><rect x="1" y="0.5" width="8" height="9" rx="1"/><rect x="2.5" y="2" width="5" height="2" fill="#1f6f9f"/></svg>020 7946 0101</span>
    <span class="footer-item"><svg viewBox="0 0 10 10"><rect x="0.5" y="2" width="9" height="6.5"/><path d="M0.5 2 L5 5.5 L9.5 2" fill="none" stroke="#1f6f9f" stroke-width="0.8"/></svg>yourmail@kt7staffing-example.com</span>
  </footer>
</article>

<section class="card card--front">
  <div class="card__strip card__strip--top"></div>
  <div class="wordmark">KT7 STAFFING</div>
  <div class="card__person">
    <div class="card__name">Your Name</div>
    <div class="card__role">Current Position</div>
  </div>
  <div class="card__contacts">
    <div>14 Harrow Row, City of London</div>
    <div><svg viewBox="0 0 10 10"><path d="M2 0.5 L4 0.5 L4.8 2.8 L3.6 3.8 Q4.6 5.6 6.2 6.4 L7.2 5.2 L9.5 6 L9.5 8 Q9.5 9.5 8 9.5 Q0.5 9 0.5 2 Q0.5 0.5 2 0.5 Z"/></svg>020 7946 0101</div>
    <div><svg viewBox="0 0 10 10"><rect x="1" y="0.5" width="8" height="9" rx="1"/></svg>020 7946 0101</div>
    <div><svg viewBox="0 0 10 10"><rect x="0.5" y="2" width="9" height="6.5"/></svg>yourmail@kt7staffing-example.com</div>
  </div>
  <div class="card__strip card__strip--bottom">www.kt7staffing-example.com</div>
</section>

<section class="card card--back">
  <div class="card__skyline" role="img" aria-label="Photograph of a city skyline with office towers"></div>
  <svg style="position:absolute;left:0;top:62px;width:248px;height:30px" viewBox="0 0 248 30" aria-hidden="true">
    <path d="M0 30 L0 18 Q110 0 248 14 L248 30 Z" fill="#d7eef8"/>
  </svg>
  <div class="wordmark">KT7 STAFFING</div>
  <div class="card__strip card__strip--bottom">www.kt7staffing-example.com</div>
</section>

<div class="project-mark">KT7 STAFFING</div>
<div class="project-rule"></div>
<div class="project-title">Stationery Design Project</div>

</body>
</html>
```